Redesign current business card for food company

i would like to redesign my business card. our company is food company, our product range from chips, juices, milk and etc (mostly dried food stuff).
I want o keep same logo but , the rest is open to new design.
you can check at our website about our company www.torvikeats.com

Target Market(s)

most of food company

Industry/Entity Type

Business

Contact Information for Business Card

I want to keep more to blue color...

Colors
3176b5
abd036

Requirements
Must have
• our old logo
Nice to have
• we do not mind to have nice material on bus card in order to accomplish nice design. for example: using spot uv, embossed and etc.

```html
<!DOCTYPE html>
<html lang="en">
<head>
<meta charset="utf-8">
<title>Torvik Enterprises Business Card</title>
<link href="https://fonts.googleapis.com/css2?family=Nunito:wght@400;600;700&display=swap" rel="stylesheet">
<style>
  :root {
    --brand-blue: #3a5bc7;
    --ink: #2a2a2a;
    --ink-soft: #4a4a4a;
    --card: #f7f7f7;
    --stage: #e6e6e6;
    --divider: #7a7fd6;
    --ring-yellow: #f2d65a;
    --ring-green: #a9d25a;
    --ring-red: #e2775a;
  }
  * { box-sizing: border-box; margin: 0; padding: 0; }
  html, body { width: 1200px; height: 780px; overflow: hidden; }
  body {
    background: var(--stage);
    font-family: "Nunito", Arial, sans-serif;
    display: flex;
    align-items: center;
    justify-content: center;
    gap: 50px;
  }
  .card {
    width: 525px;
    height: 300px;
    background: var(--card);
    border-radius: 18px;
    box-shadow: 0 2px 8px rgba(0,0,0,0.12);
    position: relative;
    overflow: hidden;
  }
  .wordmark {
    font-weight: 700;
    color: var(--brand-blue);
    line-height: 1;
  }
  /* Front */
  .front-name {
    position: absolute;
    left: 30px;
    width: 226px;
    top: 0;
    bottom: 0;
    display: flex;
    align-items: center;
    justify-content: center;
  }
  .front-name .wordmark { font-size: 64px; }
  .divider {
    position: absolute;
    left: 268px;
    top: 34px;
    width: 1px;
    height: 232px;
    background: var(--divider);
  }
  .details {
    position: absolute;
    left: 288px;
    top: 30px;
    right: 16px;
    color: var(--ink);
  }
  .company { font-size: 19px; font-weight: 600; margin-bottom: 8px; }
  .person { font-size: 17px; font-weight: 700; color: var(--brand-blue); line-height: 1.1; }
  .title { font-size: 12px; color: var(--ink-soft); margin-bottom: 14px; }
  .address { font-size: 12.5px; margin-bottom: 4px; }
  .contact-list { list-style: none; font-size: 12.5px; }
  .contact-list li { display: flex; align-items: center; gap: 7px; line-height: 1.55; }
  .contact-list svg { width: 12px; height: 12px; flex: none; }
  .web { font-size: 12.5px; margin-top: 6px; }
  .web span { color: var(--brand-blue); }
  /* Back */
  .ring-art {
    position: absolute;
    left: 50%; top: 50%;
    width: 270px; height: 270px;
    transform: translate(-50%, -50%);
    border-radius: 50%;
    background: radial-gradient(circle, transparent 0 92px, var(--ring-yellow) 93px, var(--ring-green) 115px, var(--ring-red) 135px, transparent 136px);
    opacity: 0.85;
  }
  .back-name {
    position: absolute;
    left: 50%; top: 50%;
    transform: translate(-50%, -50%);
  }
  .back-name .wordmark { font-size: 42px; }
</style>
</head>
<body>
  <section class="card card-front">
    <div class="front-name">
      <span class="wordmark">torvik</span>
    </div>
    <div class="divider"></div>
    <div class="details">
      <p class="company">Torvik Enterprises Corp.</p>
      <p class="person">Marcus Halvorsen</p>
      <p class="title">President</p>
      <p class="address">2417 W. Elm St Ontario, CA 91762</p>
      <ul class="contact-list">
        <li>
          <svg viewBox="0 0 12 12"><path d="M2 1h3l1 3-1.5 1a6 6 0 0 0 2.5 2.5L8 6l3 1v3a1 1 0 0 1-1 1A9 9 0 0 1 1 2a1 1 0 0 1 1-1z" fill="#3a5bc7"/></svg>
          555-214-3380
        </li>
        <li>
          <svg viewBox="0 0 12 12"><rect x="1" y="4" width="10" height="6" rx="1" fill="#3a5bc7"/><rect x="3" y="1" width="6" height="3" fill="#3a5bc7"/><rect x="3" y="6" width="6" height="1" fill="#fff"/></svg>
          555-214-3391
        </li>
        <li>
          <svg viewBox="0 0 12 12"><rect x="3" y="0.5" width="6" height="11" rx="1" fill="none" stroke="#555" stroke-width="1"/><rect x="5" y="9.5" width="2" height="0.8" fill="#555"/></svg>
          555 876 0142
        </li>
        <li>
          <svg viewBox="0 0 12 12"><rect x="0.5" y="2.5" width="11" height="7" fill="#3a5bc7"/><path d="M0.5 2.5 6 7l5.5-4.5" fill="none" stroke="#fff" stroke-width="1"/></svg>
          marcus@torvikeats.com
        </li>
      </ul>
      <p class="web">www.<span>torvikeats</span>.com</p>
    </div>
  </section>

  <section class="card card-back">
    <div class="ring-art" role="img" aria-label="Ring of fruit, cheese, chips, juice splashes, a picnic basket, rainbows and a sun"></div>
    <div class="back-name">
      <span class="wordmark">torvik</span>
    </div>
  </section>
</body>
</html>
```